11 x 11 Flyer Design for Social Media - Reverse Mortgages

62 or older?

A Reverse Mortgage
could be
Your Road to Financial Freedom

* No Monthly Payments
* No Income Requirements
* No Credit Score Requirements
* No Loss of Ownership

Receive cash by lump sum, monthly installments or a line of credit!!

Call us today for a Free Consultation!!
(800) 471-2965

Bluegate Financial Services, Inc.
NMLS #318760
www.bluegatehome.com

```html
<!DOCTYPE html>
<html lang="en">
<head>
<meta charset="utf-8">
<title>Reverse Mortgage Flyer – Bluegate Financial Services</title>
<link href="https://fonts.googleapis.com/css2?family=Montserrat:wght@500;700;800;900&family=Fira+Sans:wght@600&display=swap" rel="stylesheet">
<style>
  :root {
    --gold: #ac9d33;
    --blue: #1a63a8;
    --white: #ffffff;
    --ink: #111111;
  }
  * { margin: 0; padding: 0; box-sizing: border-box; }
  html, body { width: 1200px; height: 1200px; overflow: hidden; background: var(--white); }
  .flyer { position: relative; width: 1200px; height: 1200px; overflow: hidden; background: var(--white); font-family: "Montserrat", sans-serif; }

  .hero-photo {
    position: absolute; right: 0; top: 0; width: 560px; height: 460px;
    background: linear-gradient(90deg, rgba(172,157,51,0) 0%, rgba(205,200,170,.85) 35%, #d9d6c8 60%, #c9d3d8 100%);
  }
  .hero-bg { position: absolute; left: 0; top: 0; width: 1200px; height: 520px; }
  .nmls { position: absolute; right: 28px; top: 22px; font-size: 10px; font-weight: 800; color: var(--ink); }

  .kicker { position: absolute; left: 68px; top: 74px; font-size: 39px; font-weight: 700; color: var(--ink); white-space: nowrap; }
  .headline {
    position: absolute; left: 70px; top: 126px; font-size: 106px; font-weight: 900; line-height: 96px;
    color: var(--white); text-shadow: 3px 4px 6px rgba(0,0,0,.35); letter-spacing: -1px; white-space: nowrap;
  }

  .brand { position: absolute; left: 850px; top: 452px; width: 330px; display: flex; align-items: center; gap: 12px; }
  .brand-dot { width: 30px; height: 30px; border-radius: 50%; background: var(--blue); flex: none; }
  .brand-name { font-size: 25px; font-weight: 800; color: var(--blue); line-height: 1.15; }

  .couple-photo {
    position: absolute; left: 0; top: 0; width: 1200px; height: 1200px;
    background: linear-gradient(160deg, #7d97b5 38%, #3c4a60 52%, #9a8070 64%, #e6e6e6 72%);
    clip-path: polygon(120px 498px, 366px 540px, 262px 841px, 18px 841px);
  }
  .slash { position: absolute; left: 0; top: 0; }

  .benefit {
    position: absolute; height: 72px; display: flex; align-items: center; gap: 11px;
    font-family: "Fira Sans", sans-serif; font-weight: 600; font-size: 38px; line-height: 41px;
    color: var(--ink); white-space: nowrap;
  }
  .check { width: 72px; height: 72px; flex: none; }

  .cash-band {
    position: absolute; left: 0; top: 841px; width: 1200px; height: 120px; background: var(--blue);
    color: var(--white); text-align: center; font-size: 44px; font-weight: 500; line-height: 47px; padding-top: 13px;
    text-shadow: 2px 2px 3px rgba(0,0,0,.35); white-space: nowrap;
  }
  .cash-band strong { font-weight: 900; }

  .cta-band { position: absolute; left: 0; top: 961px; width: 1200px; height: 116px; display: flex; align-items: center; justify-content: center; gap: 18px; }
  .call-us { font-size: 45px; font-weight: 900; line-height: 42px; color: var(--gold); text-align: right; }
  .cta-bar { width: 12px; height: 82px; background: var(--gold); }
  .consult { font-size: 73px; font-weight: 900; color: var(--blue); letter-spacing: -1px; white-space: nowrap; }

  .contact-band { position: absolute; left: 0; top: 1077px; width: 1200px; height: 123px; background: var(--gold); display: flex; align-items: center; padding-left: 66px; gap: 18px; }
  .phone-icon { width: 72px; height: 72px; flex: none; }
  .phone { font-size: 73px; font-weight: 900; color: var(--white); text-shadow: 2px 3px 5px rgba(0,0,0,.35); letter-spacing: -1px; white-space: nowrap; }
  .contact-rule { width: 3px; height: 58px; background: var(--ink); flex: none; }
  .contact-text { font-size: 26px; color: var(--ink); line-height: 30px; white-space: nowrap; }
  .contact-text .web { font-weight: 700; }
</style>
</head>
<body>
<main class="flyer">
  <div class="hero-photo" role="img" aria-label="Photo of a smiling senior couple on a beach"></div>
  <svg class="hero-bg" width="1200" height="520" viewBox="0 0 1200 520">
    <defs>
      <linearGradient id="goldFade" x1="0" x2="1" y1="0" y2="0">
        <stop offset="0" stop-color="#ac9d33"/>
        <stop offset=".55" stop-color="#ac9d33"/>
        <stop offset=".78" stop-color="#ac9d33" stop-opacity="0"/>
      </linearGradient>
    </defs>
    <path d="M0 0 H1200 V345 C940 345 700 500 400 500 C230 500 90 440 0 390 Z" fill="url(#goldFade)"/>
    <path d="M0 390 C90 440 230 500 400 500 C700 500 940 345 1200 345 V520 H0 Z" fill="#ffffff"/>
    <path d="M0 390 C90 440 230 500 400 500 C700 500 940 345 1200 345" fill="none" stroke="#1a63a8" stroke-width="14"/>
  </svg>

  <div class="nmls">NMLS #318760</div>
  <div class="kicker">A REVERSE MORTGAGE COULD BE</div>
  <h1 class="headline">YOUR ROAD<br>TO FINANCIAL<br>FREEDOM</h1>

  <div class="brand"><span class="brand-dot"></span><span class="brand-name">Bluegate Financial Services, Inc.</span></div>

  <div class="couple-photo" role="img" aria-label="Photo of a laughing senior couple taking a selfie"></div>
  <svg class="slash" width="1200" height="1200" viewBox="0 0 1200 1200">
    <polygon points="382,606 330,796 262,841 352,662" fill="#ac9d33"/>
  </svg>

  <div class="benefit" style="left:386px;top:619px;">
    <svg class="check" viewBox="0 0 72 72"><circle cx="36" cy="36" r="31" fill="none" stroke="#ac9d33" stroke-width="7"/><path d="M22 37 L32 47 L51 27" fill="none" stroke="#ac9d33" stroke-width="7" stroke-linecap="round" stroke-linejoin="round"/></svg>
    <span>No Monthly<br>Payments</span>
  </div>
  <div class="benefit" style="left:745px;top:619px;">
    <svg class="check" viewBox="0 0 72 72"><circle cx="36" cy="36" r="31" fill="none" stroke="#ac9d33" stroke-width="7"/><path d="M22 37 L32 47 L51 27" fill="none" stroke="#ac9d33" stroke-width="7" stroke-linecap="round" stroke-linejoin="round"/></svg>
    <span>No Credit Score<br>Requirements</span>
  </div>
  <div class="benefit" style="left:360px;top:726px;">
    <svg class="check" viewBox="0 0 72 72"><circle cx="36" cy="36" r="31" fill="none" stroke="#ac9d33" stroke-width="7"/><path d="M22 37 L32 47 L51 27" fill="none" stroke="#ac9d33" stroke-width="7" stroke-linecap="round" stroke-linejoin="round"/></svg>
    <span>No Income<br>Requirements</span>
  </div>
  <div class="benefit" style="left:719px;top:726px;">
    <svg class="check" viewBox="0 0 72 72"><circle cx="36" cy="36" r="31" fill="none" stroke="#ac9d33" stroke-width="7"/><path d="M22 37 L32 47 L51 27" fill="none" stroke="#ac9d33" stroke-width="7" stroke-linecap="round" stroke-linejoin="round"/></svg>
    <span>No Loss of<br>Ownership</span>
  </div>

  <div class="cash-band">
    <strong>RECEIVE CASH</strong> BY LUMP SUM, MONTHLY<br>INSTALLMENTS OR A LINE OF CREDIT!!
  </div>

  <div class="cta-band">
    <div class="call-us">CALL US<br>TODAY</div>
    <div class="cta-bar"></div>
    <div class="consult">FREE CONSULTATION!!</div>
  </div>

  <div class="contact-band">
    <svg class="phone-icon" viewBox="0 0 72 72">
      <path d="M14 10 L24 8 L31 24 L24 29 C27 38 34 45 43 48 L48 41 L64 48 L62 58 C60 63 55 65 50 64 C30 60 12 42 8 22 C7 17 9 12 14 10 Z" fill="none" stroke="#111" stroke-width="4" stroke-linejoin="round"/>
      <path d="M40 20 A12 12 0 0 1 52 32 M40 11 A21 21 0 0 1 61 32 M40 2 A30 30 0 0 1 70 32" fill="none" stroke="#111" stroke-width="4" stroke-linecap="round"/>
    </svg>
    <div class="phone">(800) 471-2965</div>
    <div class="contact-rule"></div>
    <div class="contact-text">Bluegate Financial Services, Inc.<br><span class="web">www.bluegatehome.com</span></div>
  </div>
</main>
</body>
</html>
```